■レイアウトの希望について
◎全体の左右のサイズは、1000px~1100pxくらいでお願いします。
※左右のサイドにナビを入れる場合は、左右300pxでお願いします。
◎現在のレイアウトは無視してください。
◎重要箇所を目立たせて、全体的にバランスよく配置させてください。
※重要箇所の順位は以下の通りです。
(1)検索ページへの入り口ブロック
(2)記事ページへのナビゲーション
(3)「イチオシ学生会館紹介サイト」と「オススメ学生会館」
(4)「学生会館以外のお部屋探し」
(5)「TOPICS」と「オススメ情報」
※見本のPDFは左ナビがあるようにレイアウトしていますが、トップページは2カラムにせず、1カラムでもかまいません。
(トップページに入れたいブロックを記載しただけですのでレイアウトの希望ではありません)
ただし、サブページは左右どちらかにナビを置く形の2カラムでお願いします。
(サブページのナビに入れるのは、記事ページへのナビゲーションと「学生会館以外のお部屋探し」のみです)

■デザインの希望について
◎落ち着いた感じのバランスの良いデザイン案が希望です。
※色数を多く使ったごちゃごちゃした配置は好みではありません。
※色は派手な感じでなく落ち着いた色が希望ですが、くすんだ色は好みではありません。
◎以前にカナデルムで依頼して作成した下記サイトもご参照ください。
http://www.minorisou-kb.net/
http://www.tq4z.net/
http://www.finuyama.com/
http://274.kzo.jp/torihey.net/
※一番下のみ現在作成中のため仮URLです。(全ページは完成していません)

■その他の希望について
◎ヘッダーはスマホサイズになった場合のことも考えて作成してください。
◎提案内で使用するイメージ画像は無料の素材サイトか、有料画像を使用する場合は、ZOLVEをご利用ください。
https://zolve-foto.jp/
※現在サイト内にある画像を使用いただく形でもかまいません。

なお、初回のご提案はできるだけ締切日の2日前までにお願いします。
ギリギリの場合は修正依頼が間に合わず、候補になる良いご提案でも見送る場合がありますので..。

以上になりますので、ご提案のほど、よろしくお願いいたします。
http://www.hoshinokiryo-x.net/
基本的にはお任せですが、派手な色やくすんだ色は避けてください。(バランスの良い、落ち着いた色が希望)
JPG・PNGはどちらでもかまいません。
残り2日になりましたが、提案がないので締切日を延長いたします。

依頼詳細にも記載しましたが、できるだけ締切日の2日前までに初回のご提案をお送りいただけましたら幸いです。

その他、ご要望などがございましたら、メッセージからお送りください。
ロゴは現在のものは使用せず、見本と同様の一般的な横長のものを希望します。
(ロゴではなくて書体をそのまま使用する形でもかまいません)
弊社希望の「全体の左右のサイズは、1000px~1100pxくらい」とうのは、実際に文章や画像が入る本文(左右ナビが入る場合はその外側まで)のサイズになりますので、ご確認ください。

なお、すでにご提案を作成中の場合で、上記に当てはまらない場合はそのまま進めていただいてもかまいません。

とりあえず、デザインが分かれば問題ありませんので..。

※実際にお仕事を依頼することになった場合は、修正をお願いします。
お仕事が決まったあとに作成していただく、サブページのレイアウトを作成しましたので添付します。

決定したトップページと同じ方向性で、こちらのサブページも作成いただく形でお願いします。
今月末まで多忙になり、選考作業や細かい修正依頼作業がすぐにはできそうもないので、締切日をギリギリまで延ばさせていただきます。

必ず当選者は選定させていただきますので、よろしくお願いいたします。

また、依頼金額も若干アップさせていただきました。

全体的なバランスが良く、ごちゃごちゃしていなくて、統一感があり落ち着いた感じのご提案でした。

ご提案をいただき、ありがとうございました。
部分的には気に入ったご提案もあったのですが、全体的なバランスやメリハリといった点で、採用した案を選びました。
申し訳ございませんがご了承ください。
なお、今後も複数サイトのリニューアル依頼をカナデルムに出しますので、機会がございましたら、よろしくお願いいたします。

```html
<!DOCTYPE html>
<html lang="ja">
<head>
<meta charset="utf-8">
<title>すみかリンク</title>
<link href="https://fonts.googleapis.com/css2?family=Noto+Sans+JP:wght@400;500;700&family=M+PLUS+Rounded+1c:wght@700;800&display=swap" rel="stylesheet">
<style>
:root{
  --blue:#3fa9e0;
  --blue-dark:#1f7fbf;
  --navy:#2a4a6b;
  --sky:#e4f3fb;
  --sky-deep:#cfe8f6;
  --yellow:#f7d81f;
  --gray-bg:#eef0f1;
  --line:#dfe5ea;
  --text:#4a5561;
  --muted:#8a96a2;
  --white:#fff;
}
*{margin:0;padding:0;box-sizing:border-box}
html,body{width:688px;height:1200px;overflow:hidden;background:var(--white)}
body{font-family:"Noto Sans JP",sans-serif;color:var(--text);position:relative;font-size:7px}
.abs{position:absolute}

/* header */
.topline{left:0;top:0;width:688px;height:3px;background:var(--blue)}
.site-name{left:52px;top:12px;font-weight:700;font-size:12px;color:var(--blue-dark);line-height:16px}
.tagline{left:140px;top:17px;font-size:6px;color:var(--muted);white-space:nowrap}
.gnav{left:52px;top:40px;width:584px;height:24px;display:flex;border-bottom:2px solid var(--sky-deep)}
.gnav a{flex:1;display:flex;align-items:center;justify-content:center;gap:5px;font-size:7px;color:var(--text);text-decoration:none;border-right:1px solid var(--line)}
.gnav a:last-child{border-right:none}
.gnav a i{width:10px;height:10px;border-radius:50%;background:var(--blue);display:block}

/* hero */
.hero{left:0;top:76px;width:688px;height:228px;background:var(--gray-bg);overflow:hidden}
.slide-side{top:14px;width:150px;height:200px;background:linear-gradient(135deg,#e9e3d8,#f6f4ef);opacity:.55}
.slide-main{left:150px;top:8px;width:388px;height:212px;background:linear-gradient(120deg,#f5efe4 0%,#fbf8f2 45%,#e8e2d6 100%)}
.badge{left:200px;top:72px;width:140px;height:88px;background:var(--yellow);border-radius:6px;text-align:center;padding-top:16px}
.badge small{display:block;font-size:6px;color:var(--navy);margin-bottom:8px}
.badge b{font-family:"Noto Sans JP",sans-serif;font-weight:700;font-size:16px;color:var(--navy);line-height:1.4;display:block}
.arrow{top:97px;width:22px;height:22px;border-radius:50%;background:var(--yellow);display:flex;align-items:center;justify-content:center}
.dots{left:0;top:309px;width:688px;display:flex;justify-content:center;gap:5px}
.dots i{width:5px;height:5px;border-radius:50%;background:#c9d2d8;display:block}
.dots i.on{background:var(--blue)}

/* menu */
.menu{left:92px;top:326px;width:112px;border:1px solid var(--line)}
.menu h3{background:var(--blue);color:#fff;font-size:7px;font-weight:700;height:20px;display:flex;align-items:center;padding-left:8px;gap:4px}
.menu li{list-style:none;height:19px;border-top:1px solid var(--line);display:flex;align-items:center;padding-left:8px;gap:4px;font-size:6px}
.menu li::before{content:"";width:4px;height:4px;border-radius:50%;background:var(--blue)}

/* search */
.search-h{left:218px;top:328px;font-size:8px;font-weight:700;color:var(--navy);display:flex;align-items:center;gap:4px}
.search-h i{width:9px;height:9px;border-radius:50%;border:2px solid var(--blue);display:block}
.search-box{left:218px;top:346px;width:372px;height:30px;background:var(--gray-bg);padding:5px}
.search-input{width:280px;height:20px;background:#fff;border:1px solid var(--line)}
.search-btn{left:290px;top:5px;width:77px;height:20px;background:var(--blue);color:#fff;font-size:8px;font-weight:700;display:flex;align-items:center;justify-content:center}
.notes{left:222px;top:382px;font-size:5.5px;color:var(--muted);line-height:1.7}
.tiles{left:218px;top:412px;width:372px;display:flex;gap:9px}
.tile{flex:1;height:80px;background:var(--blue);border-radius:3px;position:relative;display:flex;justify-content:center;padding-top:14px}
.tile span{position:absolute;left:6px;right:6px;bottom:6px;height:16px;background:#fff;border-radius:2px;font-size:7px;font-weight:700;color:var(--blue-dark);display:flex;align-items:center;justify-content:center}

/* recommended */
.band{left:0;top:530px;width:688px;height:250px;background:linear-gradient(180deg,var(--sky-deep) 0%,var(--sky) 55%,#f6fbfe 100%)}
.sec-h{width:688px;left:0;text-align:center;font-family:"M PLUS Rounded 1c",sans-serif;font-weight:700;font-size:11px;color:var(--navy)}
.sec-h i{display:block;width:16px;height:16px;margin:0 auto 4px;border-radius:50%;background:var(--navy)}
.cards{left:92px;top:628px;width:494px;display:flex;gap:8px}
.card{flex:1;background:#fff;height:132px;box-shadow:0 1px 3px rgba(0,0,0,.08)}
.card .ph{height:92px;background:linear-gradient(160deg,#bfe0f3,#eef4f2 60%,#d9dcd2)}
.card p{font-size:6px;padding:6px;line-height:1.6}

/* sites */
.banners{left:115px;top:880px;width:450px;display:flex;gap:14px}
.bnr{flex:1;height:56px;border:1px solid var(--line);display:flex;align-items:center;justify-content:center;font-size:9px;font-weight:700;color:#d0486e;gap:5px}
.bnr i{width:8px;height:8px;border-radius:50%;background:#d0486e;display:block}
.bnr.mid{color:var(--navy)} .bnr.mid i{background:var(--navy)}
.bnr.pink{background:#f6e9f4;color:#9b5fa0} .bnr.pink i{background:#9b5fa0}
.sarrow{top:900px;width:14px;height:14px;display:flex;align-items:center;justify-content:center}

/* bottom */
.bottom{left:0;top:964px;width:688px;height:236px;background:var(--sky)}
.news{left:92px;top:978px;width:396px;background:#fff;height:170px}
.tabs{display:flex;height:20px}
.tabs span{width:80px;display:flex;align-items:center;justify-content:center;font-size:7px;font-weight:700}
.tabs .on{background:var(--blue);color:#fff}
.tabs .off{background:var(--gray-bg);color:var(--blue-dark);margin-left:auto}
.news ul{padding:6px 10px}
.news li{list-style:none;display:flex;align-items:center;gap:6px;height:22px;border-bottom:1px dashed var(--line);font-size:6px}
.news li b{background:var(--blue);color:#fff;font-weight:500;font-size:5px;padding:1px 4px;border-radius:2px}
.side{left:502px;top:970px;width:88px;height:176px;background:#fff;padding:8px}
.side h4{font-size:7px;font-weight:700;color:var(--blue-dark);text-align:center;line-height:1.5;margin-bottom:6px}
.side .row{display:flex;gap:4px;align-items:center;margin-bottom:6px;font-size:5.5px}
.side .row div{width:28px;height:24px;background:linear-gradient(135deg,#d6e8f2,#f2efe8);flex:none}
.pagetop{left:600px;top:1152px;width:36px;height:36px;border-radius:50%;background:var(--navy);color:#fff;font-size:5.5px;font-weight:700;display:flex;flex-direction:column;align-items:center;justify-content:center;gap:1px}
</style>
</head>
<body>

<div class="abs topline"></div>
<div class="abs site-name">すみかリンク</div>
<div class="abs tagline">首都圏の学生会館・学生寮の情報サイト</div>
<nav class="abs gnav">
  <a href="#"><i></i>学生会館とは</a>
  <a href="#"><i></i>入館までの流れ</a>
  <a href="#"><i></i>よくある質問</a>
  <a href="#"><i></i>学生会館の選び方</a>
</nav>

<section class="abs hero">
  <div class="abs slide-side" style="left:-10px"></div>
  <div class="abs slide-side" style="left:548px"></div>
  <div class="abs slide-main" role="img" aria-label="明るい部屋でノートパソコンを使う女子学生の写真"></div>
  <div class="abs badge"><small>キャンパスライフを応援!!</small><b>学生寮さがしは<br>すみかリンク</b></div>
  <div class="abs arrow" style="left:62px"><svg width="8" height="8" viewBox="0 0 8 8"><path d="M5.5 1 2.5 4l3 3" stroke="#2a4a6b" stroke-width="1.5" fill="none"/></svg></div>
  <div class="abs arrow" style="left:604px"><svg width="8" height="8" viewBox="0 0 8 8"><path d="M2.5 1l3 3-3 3" stroke="#2a4a6b" stroke-width="1.5" fill="none"/></svg></div>
</section>
<div class="abs dots"><i class="on"></i><i></i><i></i><i></i></div>

<aside class="abs menu">
  <h3>≡ メニュー</h3>
  <ul>
    <li>学生会館の魅力</li><li>設備と食事について</li><li>セキュリティ体制</li><li>費用のめやす</li>
    <li>入館の流れ</li><li>保護者の方へ</li><li>よくある質問</li><li>お問い合わせ</li>
  </ul>
</aside>

<div class="abs search-h"><i></i>学校名で探す</div>
<div class="abs search-box">
  <div class="search-input"></div>
  <div class="abs search-btn">検　索</div>
</div>
<div class="abs notes">
  ・学校名の一部を入力して検索してください<br>
  ・通学時間の目安も一緒に表示されます
</div>
<div class="abs tiles">
  <div class="tile"><svg width="26" height="30" viewBox="0 0 26 30"><rect x="3" y="1" width="20" height="22" rx="4" fill="none" stroke="#fff" stroke-width="2"/><rect x="7" y="5" width="12" height="8" fill="#fff"/><circle cx="9" cy="18" r="1.8" fill="#fff"/><circle cx="17" cy="18" r="1.8" fill="#fff"/><path d="M7 24 4 29M19 24l3 5" stroke="#fff" stroke-width="2"/></svg><span>路線から探す</span></div>
  <div class="tile"><svg width="26" height="30" viewBox="0 0 26 30"><path d="M13 2a8 8 0 0 0-8 8c0 6 8 14 8 14s8-8 8-14a8 8 0 0 0-8-8z" fill="#fff"/><circle cx="13" cy="10" r="3" fill="#3fa9e0"/><ellipse cx="13" cy="27" rx="9" ry="2" fill="none" stroke="#fff" stroke-width="1.5"/></svg><span>地域から探す</span></div>
  <div class="tile"><svg width="30" height="30" viewBox="0 0 30 30"><path d="M3 24h24M6 24V12l9-6 9 6v12" fill="none" stroke="#fff" stroke-width="2"/><rect x="12" y="15" width="6" height="9" fill="#fff"/></svg><span>学校から探す</span></div>
</div>

<section class="abs band"></section>
<h2 class="abs sec-h" style="top:540px"><i></i>オススメ学生会館</h2>
<div class="abs cards">
  <div class="card"><div class="ph" role="img" aria-label="白い外観の学生会館の写真"></div><p>女子専用・食事付き<br>駅から徒歩5分</p></div>
  <div class="card"><div class="ph" role="img" aria-label="住宅街に建つ学生会館の写真"></div><p>男女別フロア<br>駅から徒歩8分</p></div>
  <div class="card"><div class="ph" role="img" aria-label="新築の学生会館の写真"></div><p>家具家電付き<br>駅から徒歩3分</p></div>
  <div class="card"><div class="ph" role="img" aria-label="青空の下の学生会館の写真"></div><p>管理人常駐<br>駅から徒歩6分</p></div>
</div>

<h2 class="abs sec-h" style="top:812px"><i style="background:var(--blue)"></i>イチオシ学生会館紹介サイト</h2>
<div class="abs sarrow" style="left:92px"><svg width="8" height="10" viewBox="0 0 8 10"><path d="M6 1 2 5l4 4" stroke="#8a96a2" stroke-width="1.5" fill="none"/></svg></div>
<div class="abs banners">
  <div class="bnr"><i></i>女子学生寮ナビ</div>
  <div class="bnr mid"><i></i>学生寮ひろば</div>
  <div class="bnr pink"><i></i>ミライ女子寮</div>
</div>
<div class="abs sarrow" style="left:582px"><svg width="8" height="10" viewBox="0 0 8 10"><path d="M2 1l4 4-4 4" stroke="#8a96a2" stroke-width="1.5" fill="none"/></svg></div>

<section class="abs bottom"></section>
<div class="abs news">
  <div class="tabs"><span class="on">オススメ情報</span><span class="off">TOPICS</span></div>
  <ul>
    <li><b>NEW</b>新年度の入館予約を受け付けています</li>
    <li><b>NEW</b>春休み期間の見学会のお知らせ</li>
    <li><b>INFO</b>女子専用の学生会館を新たに掲載しました</li>
    <li><b>INFO</b>食事付き物件の特集ページを公開しました</li>
    <li><b>INFO</b>保護者向けの説明資料を更新しました</li>
    <li><b>INFO</b>年末年始の営業日についてのご案内</li>
  </ul>
</div>
<aside class="abs side">
  <h4>学生会館以外の<br>お部屋探し</h4>
  <div class="row"><div role="img" aria-label="ワンルームの室内写真"></div>学生マンション</div>
  <div class="row"><div role="img" aria-label="シェアハウスの室内写真"></div>シェアハウス</div>
  <div class="row"><div role="img" aria-label="賃貸アパートの外観写真"></div>賃貸アパート</div>
</aside>
<div class="abs pagetop"><svg width="8" height="6" viewBox="0 0 8 6"><path d="M1 5l3-3 3 3" stroke="#fff" stroke-width="1.5" fill="none"/></svg>PAGE TOP</div>

</body>
</html>
```